Harborline Frame Construction Needs business card

Hey we are in need of business card designs. I have upload our logo as a guideline, but free feel to run with it or come up with something unique.
Pls have fun with it and be creative. the name says it all!
i will give some directions after i see a few entries..
Logo source file has been uploaded..
Hey because of the logo is so colourful already.
Can we have a few submissions with less colour.
Also we are looking for clever/hidden/descriptive business card.

```html
<!DOCTYPE html>
<html lang="en">
<head>
<meta charset="utf-8">
<title>Harborline Frame Construction – Business Card</title>
<link rel="stylesheet" href="https://fonts.googleapis.com/css2?family=Montserrat:wght@400;600;700&family=Exo+2:wght@400;600&display=swap">
<style>
  :root {
    --bg: #d9d9d9;
    --card: #f3f3f3;
    --blue: #2e7fc6;
    --blue-deep: #1f5ea3;
    --red: #d9333a;
    --ink: #4d4d4d;
    --name-blue: #2f7dc0;
    --white: #ffffff;
  }
  * { margin: 0; padding: 0; box-sizing: border-box; }
  html, body { width: 1200px; height: 750px; overflow: hidden; }
  body {
    background: var(--bg);
    display: flex;
    align-items: center;
    justify-content: center;
    gap: 60px;
    font-family: "Montserrat", sans-serif;
  }
  .card {
    position: relative;
    width: 520px;
    height: 300px;
    border-radius: 24px;
    background: var(--card);
    overflow: hidden;
    box-shadow: 0 6px 18px rgba(0,0,0,0.18);
  }
  .card-art { position: absolute; inset: 0; width: 100%; height: 100%; }

  .wordmark {
    position: absolute;
    display: flex;
    align-items: center;
    gap: 12px;
    color: var(--ink);
    font-weight: 600;
  }
  .wordmark-square { width: 34px; height: 34px; background: var(--ink); flex: none; }
  .wordmark-text { line-height: 1.15; }
  .wordmark-name { font-size: 27px; letter-spacing: 0.5px; }
  .wordmark-sub { font-size: 11px; letter-spacing: 4px; }

  .card-front .wordmark { left: 110px; top: 62px; }

  .card-back .wordmark { left: 40px; top: 70px; }
  .card-back .wordmark-name { font-size: 17px; }
  .card-back .wordmark-sub { font-size: 8px; letter-spacing: 2.5px; }
  .card-back .wordmark-square { width: 24px; height: 24px; }

  .person { position: absolute; left: 40px; bottom: 44px; }
  .person-name { font-family: "Exo 2", sans-serif; font-weight: 600; font-size: 22px; color: var(--name-blue); }
  .person-title { font-family: "Exo 2", sans-serif; font-size: 11px; letter-spacing: 2px; color: #8a8a8a; }

  .contact {
    position: absolute;
    right: 26px;
    top: 86px;
    list-style: none;
    font-family: "Exo 2", sans-serif;
    font-size: 12.5px;
    color: var(--white);
    line-height: 1.55;
  }
  .contact li { display: flex; align-items: flex-start; gap: 7px; }
  .contact svg { width: 12px; height: 12px; margin-top: 3px; flex: none; fill: var(--white); }
  .contact .indent { padding-left: 19px; }
</style>
</head>
<body>

  <section class="card card-front" aria-label="Card front">
    <svg class="card-art" viewBox="0 0 520 300" preserveAspectRatio="none" aria-hidden="true">
      <defs>
        <linearGradient id="bandFront" x1="0" y1="1" x2="1" y2="0">
          <stop offset="0" stop-color="var(--blue)"/>
          <stop offset="1" stop-color="var(--blue-deep)"/>
        </linearGradient>
      </defs>
      <path d="M0,212 C170,230 360,160 520,78 L520,300 L0,300 Z" fill="var(--red)"/>
      <path d="M0,224 C170,240 360,172 520,96 L520,300 L0,300 Z" fill="url(#bandFront)"/>
    </svg>
    <div class="wordmark">
      <span class="wordmark-square"></span>
      <span class="wordmark-text">
        <span class="wordmark-name">HARBORLINE FRAME</span><br>
        <span class="wordmark-sub">CONSTRUCTION</span>
      </span>
    </div>
  </section>

  <section class="card card-back" aria-label="Card back">
    <svg class="card-art" viewBox="0 0 520 300" preserveAspectRatio="none" aria-hidden="true">
      <defs>
        <linearGradient id="bandBack" x1="0" y1="0" x2="1" y2="1">
          <stop offset="0" stop-color="var(--blue)"/>
          <stop offset="1" stop-color="var(--blue-deep)"/>
        </linearGradient>
      </defs>
      <path d="M330,0 C300,120 250,230 150,300 L520,300 L520,0 Z" fill="var(--red)"/>
      <path d="M342,0 C314,122 266,232 170,300 L520,300 L520,0 Z" fill="var(--white)"/>
      <path d="M352,0 C326,124 280,234 186,300 L520,300 L520,0 Z" fill="url(#bandBack)"/>
    </svg>
    <div class="wordmark">
      <span class="wordmark-square"></span>
      <span class="wordmark-text">
        <span class="wordmark-name">HARBORLINE FRAME</span><br>
        <span class="wordmark-sub">CONSTRUCTION</span>
      </span>
    </div>
    <div class="person">
      <div class="person-name">Your Name</div>
      <div class="person-title">DESIGNER</div>
    </div>
    <ul class="contact">
      <li><svg viewBox="0 0 12 12"><rect x="1" y="4" width="10" height="7" rx="1"/><rect x="2" y="1" width="8" height="2.5" rx="1"/></svg>0123456789</li>
      <li><svg viewBox="0 0 12 12"><path d="M3 1 L5 3.5 L4 5 C5 7 6 8 7 8.5 L8.5 7.5 L11 9.5 L9.5 11 C5 10.5 1.5 7 1 2.5 Z"/></svg>0123456789</li>
      <li><svg viewBox="0 0 12 12"><circle cx="6" cy="6" r="5" fill="none" stroke="#fff" stroke-width="1.6"/><circle cx="6" cy="6" r="2"/></svg>yourname@website.com</li>
      <li><svg viewBox="0 0 12 12"><path d="M6 1 L11 6 L9.5 6 L9.5 11 L2.5 11 L2.5 6 L1 6 Z"/></svg>1234 A. Your Adress,</li>
      <li class="indent">City, State 123455</li>
    </ul>
  </section>

</body>
</html>
```